DTB (community bank) envelope, stationary and business cards.
Dunmore Thrift Bank
Bright & Fun-filled
Gwen Tolliver
Marketing Director
2867 Cedar Ln. and
3915 Oak Rd. Harwick, IL 60917
gwen.tolliver@dunmorethrift.com
www.dunmorethrift.com
Bank has 60 plus employees. Many various positions. Some are licensed some are not.
Licensed example: QARB ID: 820391
It would be cool to include our Mission Statement: back of card, or ???
Maximize the customer experience, within the breadth of Products and Services we offer.
Think fresh, classy, relational, sophisticated, clear, and clean. We are all about relationships and connecting with our customers... our mission statement says it. We are a true, stable authority in the Savings and Loan banking industry. We want these pieces to speak to our customers when they get them saying---"they get it" We can trust them! (A recent advertising campaign that is very relevant with our message also, “Vintage Banking with Apps!” .)
This is an example of a "cool" ad we've been running that has recieved good feedback. Just for inspiration sake.
We like the reversed version for the back of the car- Just the House Icon and Mission Statement. Please play with the presentation of these two important features. Make it look cool!
This is where we are coming from---
A guide to work with is attached, as well as below.
Pantone - 2955 is correct!
Hex #3A5675
CMYK C: 84%, M: 65%, Y: 34%, K 16%
FONTS: (Still the same)
1.Trajan Pro (Bold,ALLCAPS)- Dunmore Thrift Bank
2.Vera Humana 95 (Bold,NORMAL/ALLCAPS)- Dunmore Thrift Bank
3.Trajan Pro (Bold,ALLCAPS)- Trust Across Generations
*Our mission is to elevate the everyday banking of our members through attentive, people-first service. We do this by truly listening and shaping thoughtful answers for each member’s own goals while embracing helpful new tools. As other banks come and go, we proudly build Trust Across Generations.*
We have adopted a complimentary file that has lower case. Please use this to create the Mission Statement. SEE this attachement.

```html
<!DOCTYPE html>
<html lang="en">
<head>
<meta charset="utf-8">
<title>Dunmore Thrift Bank — Stationery Set</title>
<link href="https://fonts.googleapis.com/css2?family=Cinzel:wght@700&family=Crimson+Text:ital,wght@0,400;0,700;1,400&display=swap" rel="stylesheet">
<style>
  :root{
    --brand:#3a5675;
    --brand-mid:#8d9ab0;
    --paper:#ffffff;
    --ghost:#e7eaf0;
    --ghost-dark:#4e6987;
    --backdrop:#2f2e30;
  }
  html,body{margin:0;padding:0;overflow:hidden;background:var(--backdrop);}
  .canvas{position:relative;width:1200px;height:640px;overflow:hidden;background:var(--backdrop);}
  .piece{position:absolute;display:block;}
  .paper{fill:var(--paper);}
  .brand-fill{fill:var(--brand);}
  .ghost-fill{fill:var(--ghost);}
  .ghost-dark-fill{fill:var(--ghost-dark);}
  .stop-brand{stop-color:var(--brand);}
  .stop-mid{stop-color:var(--brand-mid);}
  .stop-white{stop-color:var(--paper);}
  .wordmark{font-family:'Cinzel',serif;font-weight:700;fill:var(--brand);letter-spacing:.02em;}
  .wordmark.reversed{fill:var(--paper);}
  .tagline{font-family:'Cinzel',serif;font-weight:700;fill:var(--brand);letter-spacing:.06em;}
  .contact{font-family:'Crimson Text',serif;fill:var(--brand);}
  .contact.reversed{fill:var(--paper);}
  .person{font-family:'Crimson Text',serif;font-weight:700;fill:var(--brand);}
  .role{font-family:'Crimson Text',serif;font-style:italic;fill:var(--brand);}
  .mission-title{font-family:'Crimson Text',serif;font-style:italic;fill:var(--paper);}
  .mission-text{font-family:'Crimson Text',serif;fill:var(--paper);}
  .rule-light{stroke:var(--paper);stroke-width:.5;opacity:.8;}
</style>
</head>
<body>
<div class="canvas">

  <!-- Presentation folder: inside pocket panel -->
  <svg class="piece folder-inside" style="left:20px;top:20px" width="210" height="297" viewBox="0 0 210 297">
    <defs>
      <linearGradient id="folder-swoosh" x1="0" y1="0" x2="1" y2="0">
        <stop offset="0" class="stop-brand"/><stop offset=".55" class="stop-mid"/><stop offset="1" class="stop-white"/>
      </linearGradient>
    </defs>
    <rect class="paper" width="210" height="297"/>
    <rect class="ghost-fill" x="120" y="170" width="62" height="62"/>
    <g transform="translate(78 18)">
      <rect class="brand-fill" width="9" height="9"/>
      <text class="wordmark" x="13" y="7" font-size="7.6">DUNMORE THRIFT BANK</text>
      <text class="tagline" x="13" y="13" font-size="4.2">TRUST ACROSS GENERATIONS</text>
    </g>
    <path fill="url(#folder-swoosh)" d="M0 176 C70 178 140 238 210 250 L210 258 C140 248 70 196 0 190Z"/>
    <path class="brand-fill" d="M0 190 C70 196 140 248 210 258 L210 297 L0 297Z"/>
  </svg>

  <!-- Presentation folder: cover panel -->
  <svg class="piece folder-cover" style="left:230px;top:20px" width="210" height="297" viewBox="0 0 210 297">
    <rect class="brand-fill" width="210" height="297"/>
    <rect class="ghost-dark-fill" x="55" y="70" width="100" height="100"/>
    <g class="contact reversed" font-size="4.4">
      <text x="12" y="244">2867 Cedar Ln. and</text>
      <text x="12" y="250">3915 Oak Rd. Harwick, IL 60917</text>
      <text x="12" y="256">630.555.0142</text>
      <text x="12" y="262">630.555.0187</text>
      <text x="12" y="268">gwen.tolliver@dunmorethrift.com</text>
      <text x="12" y="274">www.dunmorethrift.com</text>
    </g>
  </svg>

  <!-- Business card front -->
  <svg class="piece card card-front" style="left:20px;top:350px" width="200" height="115" viewBox="0 0 200 115">
    <defs>
      <linearGradient id="card-swoosh" x1="0" y1="0" x2="1" y2="0">
        <stop offset="0" class="stop-white"/><stop offset=".5" class="stop-mid"/><stop offset="1" class="stop-brand"/>
      </linearGradient>
    </defs>
    <rect class="paper" width="200" height="115" rx="10"/>
    <g transform="translate(12 12)">
      <rect class="brand-fill" width="8" height="8"/>
      <text class="wordmark" x="11" y="6.5" font-size="7">DUNMORE THRIFT BANK</text>
      <text class="tagline" x="11" y="12" font-size="3.8">TRUST ACROSS GENERATIONS</text>
    </g>
    <text class="person" x="188" y="40" font-size="8" text-anchor="end">Gwen Tolliver</text>
    <text class="role" x="188" y="47" font-size="4.8" text-anchor="end">Marketing Director</text>
    <path fill="url(#card-swoosh)" d="M0 52 C70 54 130 74 200 76 L200 82 C130 80 70 62 0 60Z"/>
    <path class="brand-fill" d="M0 60 C70 62 130 80 200 82 L200 115 L0 115Z"/>
    <g class="contact reversed" font-size="4.6">
      <text x="12" y="80">2867 Cedar Ln. and</text>
      <text x="12" y="86">3915 Oak Rd. Harwick, IL 60917</text>
      <text x="12" y="92">630.555.0142 · 630.555.0187</text>
      <text x="12" y="98">gwen.tolliver@dunmorethrift.com</text>
      <text x="12" y="104">www.dunmorethrift.com</text>
    </g>
  </svg>

  <!-- Business card back: mission statement -->
  <svg class="piece card card-back" style="left:240px;top:350px" width="200" height="115" viewBox="0 0 200 115">
    <rect class="brand-fill" width="200" height="115" rx="10"/>
    <text class="mission-title" x="100" y="20" font-size="10" text-anchor="middle">Our Mission Statement</text>
    <line class="rule-light" x1="30" y1="25" x2="170" y2="25"/>
    <g class="mission-text" font-size="5.6" text-anchor="middle">
      <text x="100" y="35">Our mission is to elevate the everyday banking</text>
      <text x="100" y="43">of our members through attentive, people-first service.</text>
      <text x="100" y="51">We do this by truly listening and shaping</text>
      <text x="100" y="59">thoughtful answers for each member’s own goals</text>
      <text x="100" y="67">while embracing helpful new tools.</text>
      <text x="100" y="75">As other banks come and go,</text>
      <text x="100" y="83">we proudly build TRUST ACROSS GENERATIONS.</text>
    </g>
    <line class="rule-light" x1="30" y1="90" x2="170" y2="90"/>
  </svg>

  <!-- Letterhead with footer wave -->
  <svg class="piece letterhead letterhead-footer" style="left:460px;top:20px" width="200" height="283" viewBox="0 0 200 283">
    <defs>
      <linearGradient id="lh1-swoosh" x1="0" y1="0" x2="1" y2="0">
        <stop offset="0" class="stop-brand"/><stop offset=".5" class="stop-mid"/><stop offset="1" class="stop-white"/>
      </linearGradient>
    </defs>
    <rect class="paper" width="200" height="283"/>
    <g transform="translate(62 14)">
      <rect class="brand-fill" width="9" height="9"/>
      <text class="wordmark" x="13" y="7" font-size="7.6">DUNMORE THRIFT BANK</text>
      <text class="tagline" x="13" y="13" font-size="4.1">TRUST ACROSS GENERATIONS</text>
    </g>
    <path fill="url(#lh1-swoosh)" d="M0 222 C60 224 120 262 200 268 L200 272 C120 270 60 238 0 236Z"/>
    <path class="brand-fill" d="M0 236 C60 238 120 270 200 272 L200 283 L0 283Z"/>
    <g class="contact reversed" font-size="3.6">
      <text x="8" y="250">2867 Cedar Ln. and</text>
      <text x="8" y="255">3915 Oak Rd. Harwick, IL 60917</text>
      <text x="8" y="260">630.555.0142 · 630.555.0187</text>
      <text x="8" y="265">gwen.tolliver@dunmorethrift.com</text>
      <text x="8" y="270">www.dunmorethrift.com</text>
    </g>
  </svg>

  <!-- Letterhead with header wave -->
  <svg class="piece letterhead letterhead-header" style="left:680px;top:20px" width="200" height="283" viewBox="0 0 200 283">
    <defs>
      <linearGradient id="lh2-swoosh" x1="0" y1="0" x2="1" y2="0">
        <stop offset="0" class="stop-white"/><stop offset=".6" class="stop-mid"/><stop offset="1" class="stop-brand"/>
      </linearGradient>
    </defs>
    <rect class="paper" width="200" height="283"/>
    <path class="brand-fill" d="M0 0 H200 V26 C150 26 120 4 0 3Z"/>
    <path fill="url(#lh2-swoosh)" d="M0 3 C120 4 150 26 200 26 L200 36 C150 36 120 8 0 6Z"/>
    <g transform="translate(10 14)">
      <rect class="brand-fill" width="8" height="8"/>
      <text class="wordmark" x="11" y="6.5" font-size="6.8">DUNMORE THRIFT BANK</text>
      <text class="tagline" x="11" y="12" font-size="3.7">TRUST ACROSS GENERATIONS</text>
    </g>
    <g class="contact" font-size="3.6" text-anchor="end">
      <text x="192" y="46">2867 Cedar Ln. and</text>
      <text x="192" y="51">3915 Oak Rd. Harwick, IL 60917</text>
      <text x="192" y="56">630.555.0142 · 630.555.0187</text>
      <text x="192" y="61">gwen.tolliver@dunmorethrift.com</text>
      <text x="192" y="66">www.dunmorethrift.com</text>
    </g>
  </svg>

  <!-- #10 envelope, sender top-left -->
  <svg class="piece envelope envelope-long-a" style="left:460px;top:330px" width="420" height="140" viewBox="0 0 420 140">
    <defs>
      <linearGradient id="dl1-swoosh" x1="0" y1="0" x2="1" y2="0">
        <stop offset="0" class="stop-white"/><stop offset=".5" class="stop-mid"/><stop offset="1" class="stop-brand"/>
      </linearGradient>
    </defs>
    <rect class="paper" width="420" height="140"/>
    <text class="person" x="14" y="16" font-size="7">Gwen Tolliver</text>
    <text class="role" x="14" y="22" font-size="4.4">Marketing Director</text>
    <g class="contact" font-size="3.9">
      <text x="14" y="31">2867 Cedar Ln. and</text>
      <text x="14" y="36">3915 Oak Rd. Harwick, IL 60917</text>
      <text x="14" y="41">630.555.0142 · 630.555.0187</text>
      <text x="14" y="46">gwen.tolliver@dunmorethrift.com</text>
      <text x="14" y="51">www.dunmorethrift.com</text>
    </g>
    <path class="brand-fill" d="M0 60 C140 62 260 110 420 116 L420 122 C260 116 140 68 0 68Z"/>
    <path fill="url(#dl1-swoosh)" d="M0 68 C140 68 260 116 420 122 L420 132 C260 126 140 92 0 96Z"/>
    <g transform="translate(170 52)">
      <text class="wordmark" x="0" y="9" font-size="11">DUNMORE THRIFT BANK</text>
      <text class="tagline" x="0" y="17" font-size="5.6">TRUST ACROSS GENERATIONS</text>
    </g>
    <text class="wordmark" x="356" y="96" font-size="24">DTB</text>
  </svg>

  <!-- #10 envelope, mark left -->
  <svg class="piece envelope envelope-long-b" style="left:460px;top:485px" width="420" height="140" viewBox="0 0 420 140">
    <defs>
      <linearGradient id="dl2-swoosh" x1="0" y1="0" x2="1" y2="0">
        <stop offset="0" class="stop-brand"/><stop offset=".5" class="stop-mid"/><stop offset="1" class="stop-white"/>
      </linearGradient>
    </defs>
    <rect class="paper" width="420" height="140"/>
    <text class="wordmark" x="14" y="40" font-size="24">DTB</text>
    <g transform="translate(150 28)">
      <text class="wordmark" x="0" y="9" font-size="11">DUNMORE THRIFT BANK</text>
      <text class="tagline" x="0" y="17" font-size="5.6">TRUST ACROSS GENERATIONS</text>
    </g>
    <path class="brand-fill" d="M0 48 C120 52 260 92 420 104 L420 110 C260 98 120 58 0 56Z"/>
    <path fill="url(#dl2-swoosh)" d="M0 56 C120 58 260 98 420 110 L420 118 C260 110 120 80 0 76Z"/>
    <text class="person" x="406" y="126" font-size="7" text-anchor="end">Gwen Tolliver</text>
    <text class="role" x="406" y="132" font-size="4.4" text-anchor="end">Marketing Director</text>
    <g class="contact" font-size="3.9">
      <text x="14" y="100">2867 Cedar Ln. and</text>
      <text x="14" y="105">3915 Oak Rd. Harwick, IL 60917</text>
      <text x="14" y="110">630.555.0142 · 630.555.0187</text>
      <text x="14" y="115">gwen.tolliver@dunmorethrift.com</text>
      <text x="14" y="120">www.dunmorethrift.com</text>
    </g>
  </svg>

  <!-- Catalog envelope front -->
  <svg class="piece envelope envelope-catalog-front" style="left:900px;top:20px" width="280" height="190" viewBox="0 0 280 190">
    <defs>
      <linearGradient id="c5-swoosh" x1="0" y1="0" x2="1" y2="0">
        <stop offset="0" class="stop-brand"/><stop offset=".5" class="stop-mid"/><stop offset="1" class="stop-white"/>
      </linearGradient>
    </defs>
    <rect class="paper" width="280" height="190"/>
    <rect class="ghost-fill" x="190" y="78" width="70" height="70"/>
    <g transform="translate(14 14)">
      <rect class="brand-fill" width="9" height="9"/>
      <text class="wordmark" x="13" y="7" font-size="8.4">DUNMORE THRIFT BANK</text>
      <text class="tagline" x="13" y="13" font-size="4.5">TRUST ACROSS GENERATIONS</text>
    </g>
    <g class="contact" font-size="4.2">
      <text x="27" y="38">2867 Cedar Ln. and</text>
      <text x="27" y="43">3915 Oak Rd. Harwick, IL 60917</text>
    </g>
    <path fill="url(#c5-swoosh)" d="M0 112 C90 114 170 156 280 164 L280 172 C170 166 90 126 0 124Z"/>
    <path class="brand-fill" d="M0 124 C90 126 170 166 280 172 L280 190 L0 190Z"/>
  </svg>

  <!-- Catalog envelope back -->
  <svg class="piece envelope envelope-catalog-back" style="left:900px;top:230px" width="280" height="190" viewBox="0 0 280 190">
    <rect class="paper" width="280" height="190"/>
    <path class="brand-fill" d="M0 0 H280 V60 Q140 135 0 60Z"/>
    <text class="wordmark reversed" x="140" y="78" font-size="14" text-anchor="middle">DTB</text>
  </svg>

</div>
</body>
</html>
```